Veltrane Hand Sanitiser Spray Product Range for International Markets

Veltrane is a new Healthcare business launching a full product range of Anti-bacterial Hand Sanitiser Spray bottles in various sizes. We have a new logo which we believe differentiates us from the competition: Veltrane - Care That Goes Further
The Product Range will comprise two distinct product solution types:
- Anti-bacterial Hand Sanitisers - Alcohol based
- Anti-bacterial Hand Sanitisers - Sensitive Non Alcohol based
Bottle sizes will comprise a range containing:
100ml, 250ml, 500ml, 1ltr, 5ltr, 10ltr
Some bottles will have Pump Sprays
The Product labelling will be attractive front packaging label combined with strong product attributes and usage indicator cues.
As a Healthcare brand our logo design is light Green. We believe that this should be combined with blues and greens balanced to create contrast and strong stand-out on-shelf.
A review of competitor brands will show some similar colour cues, however as a Healthcare brand, the colour cues Green and White are synonymous with the sector. Many existing brands are very pragmatic in their label design. i.e. #it does what is says on the tin approach#. Our brand will need strong stand-out and strong aesthetic appeal too, since it will often be left in public view and around the home and office and therefore should look as attractive as possible. There will be other brand variants in the future and thought should be given to this too - with use of colour cues.
For Competitor indicators check-out the brands on Brisklot - Pine Hollow, Dermavell and others....Thank-you!

Target Market(s)

First: Female 25 - 65
Second: Male 25 - 65

Contact Information for Business Card

Garth L. Dunmore
CEO
Veltrane Healthcare Worldwide
'Care That Goes Further'
www.VeltraneHealthcare.example
E. gldunmore@veltranehealthcare.example
T. +44 7700 900318
T. +44 118 496072

Font styles to use
Sans Serif

Colors
34a7d7
33b8a4
add136
fbee3e
b768aa

```html
<!DOCTYPE html>
<html lang="en">
<head>
<meta charset="utf-8">
<title>Veltrane Hand Sanitiser Label</title>
<link href="https://fonts.googleapis.com/css2?family=Roboto:wght@400&display=swap" rel="stylesheet">
<style>
  :root {
    --page-bg: #f4f4f6;
    --label-teal-dark: #0d4a4d;
    --label-teal: #17666a;
    --label-teal-light: #2a8e93;
    --label-ink: #ffffff;
  }
  html, body {
    margin: 0;
    padding: 0;
    width: 1200px;
    height: 1050px;
    overflow: hidden;
    background: var(--page-bg);
  }
  .label {
    position: absolute;
    left: 380px;
    top: 85px;
    width: 440px;
    height: 880px;
    border-radius: 48px;
    background: linear-gradient(180deg, var(--label-teal-dark) 0%, var(--label-teal) 45%, var(--label-teal-light) 85%, var(--label-teal) 100%);
    color: var(--label-ink);
    font-family: 'Roboto', sans-serif;
    font-weight: 400;
  }
  .brand-name {
    position: absolute;
    left: 0;
    width: 100%;
    top: 372px;
    margin: 0;
    text-align: center;
    font-size: 58px;
    font-weight: 400;
    line-height: 1;
  }
  .brand-tagline {
    position: absolute;
    left: 0;
    width: 100%;
    top: 442px;
    margin: 0;
    text-align: center;
    font-size: 9px;
    letter-spacing: 2.5px;
  }
  .solution-type, .volume {
    position: absolute;
    left: 0;
    width: 100%;
    margin: 0;
    text-align: center;
  }
  .solution-type { top: 630px; font-size: 17px; letter-spacing: 0.3px; }
  .volume { top: 672px; font-size: 21px; }
</style>
</head>
<body>
  <main class="label">
    <h1 class="brand-name">Veltrane</h1>
    <p class="brand-tagline">CARE THAT GOES FURTHER</p>
    <p class="solution-type">NON ALCOHOL BASED</p>
    <p class="volume">100ml</p>
  </main>
</body>
</html>
```